Business card needed for the Rydo of Dry Cleaning!

We need a slick business card design for a new company based out of Montreal called Casiers Plimo&Zet inc. (in French) and Plimo&Zet Lockers inc. (in English). We're the Rydo of Laundry. We offer services of dry cleaning, laundry (wash&fold), minor clothing alterations, shoe repair and parcel delivery through 24/7 secured and connected lockers. Ordres are placed through our mobile application. Real time notification are sent to customers when their order is ready for pickup. The lockers will be placed throughout the downtown area, in condo and office towers, where a high density of busy people converge. It is simple, user-friendly, and most importantly convenient. We're the out of the box dry cleaner, literally.

Target Market(s)

1) Professional workers wearing suits daily
2) Campus students living in residences
3) People using laundromats
4) Families with children/yuppies who prefer to use their time doing something else than laundry

Industry/Entity Type

Dry Cleaning

Contact Information for Business Card

Name / Annick-Solène Trudel
Title / CEO & Founder
Company Name / Casiers Plimo&Zet inc. | Plimo&Zet Lockers inc.
Website www.plimozet.ca

Requirements
Must have
• Text Logo: Plimo&Zet - Nettoyeurs 24/7 Cleaners
• Logo on one side and contact info on the other (bilingual)
• Minimalist, pure design
• "We care" for your belongings feeling
• Professional, technological, clean & fresh look
Should not have
• No busy visuals. No rainbow colors.

```html
<!DOCTYPE html>
<html lang="en">
<head>
<meta charset="utf-8">
<title>Plimo&amp;Zet Lockers inc. — Business Card</title>
<link href="https://fonts.googleapis.com/css2?family=Questrial&display=swap" rel="stylesheet">
<style>
  :root {
    --stage: #e9e6e2;
    --card: #ffffff;
    --ink: #4a4b4d;
    --ink-soft: #5d5e60;
    --brand-blue: #4bb8d9;
    --panel-blue: #2b9bc7;
    --panel-ink: #e4e6e8;
    --shadow: rgba(0, 0, 0, 0.22);
  }
  * { box-sizing: border-box; margin: 0; padding: 0; }
  html, body {
    width: 1200px;
    height: 1020px;
    overflow: hidden;
    background: var(--stage);
    font-family: "Questrial", "Century Gothic", sans-serif;
    color: var(--ink);
  }
  .canvas { position: relative; width: 1200px; height: 1020px; }

  .card {
    position: absolute;
    background: var(--card);
    box-shadow: 0 10px 24px var(--shadow);
  }
  .card--front { left: 110px; top: 34px; width: 540px; height: 308px; }
  .card--back  { left: 165px; top: 368px; width: 990px; height: 330px; }

  .wordmark {
    position: absolute;
    display: flex;
    align-items: center;
    gap: 12px;
    color: var(--ink);
  }
  .wordmark__dot {
    width: 40px; height: 40px;
    border-radius: 50%;
    background: var(--brand-blue);
    flex: none;
  }
  .wordmark__text { display: flex; flex-direction: column; line-height: 1; }
  .wordmark__name { font-size: 52px; letter-spacing: -0.5px; }
  .wordmark__sub  { font-size: 17px; letter-spacing: 5px; margin-top: 6px; padding-left: 4px; color: var(--brand-blue); }
  .wordmark__tagline { font-size: 13px; letter-spacing: 2px; margin-top: 8px; padding-left: 4px; color: var(--ink-soft); }

  .card--front .wordmark { left: 50%; top: 56%; transform: translate(-50%, -50%); }

  .card--back .wordmark { left: 110px; top: 160px; }
  .card--back .wordmark__name { font-size: 46px; }
  .card--back .wordmark__sub  { font-size: 15px; letter-spacing: 4px; }
  .card--back .wordmark__dot  { width: 32px; height: 32px; }

  .contact { position: absolute; left: 450px; top: 70px; }
  .contact__name { font-size: 28px; color: var(--ink-soft); }
  .contact__title { font-size: 18px; color: var(--brand-blue); margin-top: 4px; }
  .contact__company { font-size: 14px; color: var(--ink-soft); margin-top: 6px; }
  .contact__list { list-style: none; margin-top: 10px; }
  .contact__item {
    display: flex; align-items: center; gap: 14px;
    font-size: 17px; color: var(--ink-soft); margin-top: 7px;
  }
  .contact__icon { width: 20px; height: 15px; flex: none; }

  .panel {
    position: absolute; top: 715px; height: 305px;
    display: flex; align-items: center; justify-content: center;
  }
  .panel--light { left: 0; width: 603px; background: #f7f7f7; }
  .panel--blue  { left: 603px; width: 597px; background: var(--panel-blue); }
  .panel .wordmark { position: static; padding-top: 60px; }
  .panel .wordmark__name { font-size: 68px; }
  .panel .wordmark__sub  { font-size: 24px; letter-spacing: 7px; margin-top: 10px; }
  .panel .wordmark__dot  { width: 50px; height: 50px; }
  .panel--blue .wordmark { color: var(--panel-ink); }
  .panel--blue .wordmark__sub { color: var(--panel-ink); }
  .panel--blue .wordmark__dot { background: var(--panel-ink); }
</style>
</head>
<body>
<main class="canvas">

  <section class="card card--front" aria-label="Card front">
    <div class="wordmark">
      <span class="wordmark__dot"></span>
      <span class="wordmark__text">
        <span class="wordmark__name">Plimo&amp;Zet</span>
        <span class="wordmark__sub">Lockers inc.</span>
        <span class="wordmark__tagline">Nettoyeurs 24/7 Cleaners</span>
      </span>
    </div>
  </section>

  <section class="card card--back" aria-label="Card back">
    <div class="wordmark">
      <span class="wordmark__dot"></span>
      <span class="wordmark__text">
        <span class="wordmark__name">Plimo&amp;Zet</span>
        <span class="wordmark__sub">Lockers inc.</span>
      </span>
    </div>

    <div class="contact">
      <p class="contact__name">Annick-Solène Trudel</p>
      <p class="contact__title">Title / CEO &amp; Founder</p>
      <p class="contact__company">Casiers Plimo&amp;Zet inc. | Plimo&amp;Zet Lockers inc.</p>
      <ul class="contact__list">
        <li class="contact__item">
          <svg class="contact__icon" viewBox="0 0 18 14" aria-hidden="true">
            <rect x="0.5" y="1" width="17" height="12" fill="var(--brand-blue)"/>
            <path d="M1 1.5 L9 8 L17 1.5" fill="none" stroke="#fff" stroke-width="1.3"/>
          </svg>
          000 000 0000
        </li>
        <li class="contact__item">
          <svg class="contact__icon" viewBox="0 0 18 14" aria-hidden="true">
            <path d="M1 5 Q9 -1 17 5 L15 6.5 L12.5 5 L12.5 3.5 Q9 2.5 5.5 3.5 L5.5 5 L3 6.5 Z" fill="var(--brand-blue)"/>
            <rect x="3" y="7" width="12" height="6.5" rx="1" fill="var(--brand-blue)"/>
          </svg>
          Email@xyz.com
        </li>
        <li class="contact__item">
          <svg class="contact__icon" viewBox="0 0 18 14" aria-hidden="true">
            <g fill="none" stroke="var(--brand-blue)" stroke-width="1.1">
              <circle cx="9" cy="7" r="6"/>
              <ellipse cx="9" cy="7" rx="2.6" ry="6"/>
              <path d="M3 7 H15 M4 4 H14 M4 10 H14"/>
            </g>
          </svg>
          www.plimozet.ca
        </li>
      </ul>
    </div>
  </section>

  <section class="panel panel--light" aria-label="Logo on white">
    <div class="wordmark">
      <span class="wordmark__dot"></span>
      <span class="wordmark__text">
        <span class="wordmark__name">Plimo&amp;Zet</span>
        <span class="wordmark__sub">Lockers inc.</span>
      </span>
    </div>
  </section>

  <section class="panel panel--blue" aria-label="Logo on blue">
    <div class="wordmark">
      <span class="wordmark__dot"></span>
      <span class="wordmark__text">
        <span class="wordmark__name">Plimo&amp;Zet</span>
        <span class="wordmark__sub">Lockers inc.</span>
      </span>
    </div>
  </section>

</main>
</body>
</html>
```